Wordpress Design Project (Millbrook)

We need a wordpress design for an established auction and real estate company based in California. The winning design will incorporate a creative layout, pleasing color scheme and logo in a very professional and clean manner.

Industry/Entity Type

Real Estate

Requirements
Must have
• Client likes the overall look of http://vornpeq.com/. Site will use the logo colors and maybe complimentary highlight color. Note from client: "“It's important that the appearance of the site will be unique and easily recognizable. In general try to avoid too many colors especially bright and negative contention colors such as bright red, orange, yellow and such. "

The layout should be close as the mentioned reference site except the slideshow (image attached) should be placed below navigation, perhaps at top of content area for the page. Sidebar widgets will include:
- SMS signup form
- Register to bid call to action (as in reference site)
- Email signup form (with only "enter email" field)
- Blog feature "News & Events"
- Social media icons for facebook, twitter, google+, RSS

Navigation:
1) Home
2) Auctions
3) Online Auctions
4) Past Auctions
5) About Us
6) FAQ
7) Blog
8) Contact Us
Nice to have
• Site will have drop-down menus, idea of these would be nice for any of the primary navigation tabs.
Should not have
• please use no auction gavels in the design

```html
<!DOCTYPE html>
<html lang="en">
<head>
<meta charset="utf-8">
<title>Millbrook Auctions</title>
<link href="https://fonts.googleapis.com/css2?family=Ubuntu:wght@400;500;700&family=Arimo:wght@400;700&display=swap" rel="stylesheet">
<style>
:root{
  --teal:#0f6b60;
  --teal-dark:#0a4f47;
  --teal-light:#1b8a7c;
  --maroon:#7a2a32;
  --ink:#333;
  --muted:#555;
  --panel:#f6f6f6;
  --line:#d6d6d6;
  --dark:#1e1e1e;
  --drop:#3a3a3a;
}
*{box-sizing:border-box;margin:0;padding:0}
html,body{width:1133px;height:1200px;overflow:hidden}
body{position:relative;background:linear-gradient(#f2f2f2,#fff 300px);font-family:"Arimo",Arial,sans-serif;color:var(--ink)}
.abs{position:absolute}
.topbar{left:0;top:0;width:1133px;height:8px;background:var(--teal)}
.brand{left:96px;top:40px;display:flex;align-items:center;gap:10px}
.brand-mark{width:28px;height:28px;background:var(--teal)}
.brand-name{font-family:"Ubuntu",sans-serif;font-weight:700;font-size:26px;color:var(--teal);line-height:1.05}
.tagline{left:340px;top:66px;width:420px;text-align:center;font-family:"Ubuntu",sans-serif}
.tagline h1{font-size:27px;font-weight:700;color:var(--teal)}
.tagline p{font-size:20px;font-weight:500;color:#3a3a3a;margin-top:2px}
.phone{left:810px;top:22px;display:flex;align-items:center;gap:12px}
.phone span{font-family:"Ubuntu",sans-serif;font-weight:700;font-size:24px;color:var(--teal)}
.connect{left:880px;top:78px;font-family:"Ubuntu",sans-serif;font-style:italic;font-size:14px;color:#444}
.social{left:874px;top:103px;display:flex;gap:8px}
.social span{width:31px;height:31px;background:#4a4a4a;display:block}
.nav{left:88px;top:151px;width:953px;height:47px;background:linear-gradient(var(--teal-light),var(--teal));border-radius:22px 22px 0 0;display:flex;padding-left:37px}
.nav a{font-size:14px;color:#fff;text-decoration:none;display:flex;align-items:center;padding:0 27px;border-left:1px solid rgba(0,0,0,.2);border-right:1px solid rgba(255,255,255,.12)}
.nav a.active{background:rgba(0,0,0,.1)}
.drop{left:319px;top:198px;width:178px;height:132px;background:var(--drop);padding:6px 5px}
.drop a{display:block;color:#fff;font-size:13px;text-decoration:none;height:30px;line-height:30px;padding-left:23px}
.drop a.on{background:var(--teal)}
.side-box{left:93px;width:234px;background:var(--panel);border:1px solid #e2e2e2}
.side-title{margin:4px;height:34px;background:linear-gradient(var(--teal-light),var(--teal));color:#fff;font-family:"Ubuntu",sans-serif;font-weight:700;font-size:16px;line-height:34px;padding-left:9px}
.field{height:26px;border:1px solid #ccc;border-radius:8px;background:#fff;font-size:11px;color:#666;padding-left:9px;line-height:24px;font-family:"Ubuntu",sans-serif}
.btn-dark{background:#333;color:#fff;font-family:"Ubuntu",sans-serif;font-style:italic;font-weight:700;font-size:11px;display:inline-block;padding:6px 10px}
.phone-art{left:170px;top:42px;width:55px;height:95px;border-radius:8px;background:linear-gradient(#4caf50,#1b5e20)}
.register{left:80px;top:390px;width:268px;height:218px}
.news-item{font-size:12.5px;line-height:17px;color:#444;padding:9px 0 6px 18px;border-bottom:1px dashed #ccc;position:relative;text-align:justify}
.news-item:before{content:"";position:absolute;left:4px;top:15px;border:3px solid transparent;border-left:5px solid var(--teal)}
.slide{left:370px;top:215px;width:670px;height:278px;background:#fff;border:1px solid #ddd;border-radius:0 0 14px 0;padding:10px}
.slide-img{width:100%;height:100%;background:linear-gradient(110deg,#6a4a2e,#b88a4e 45%,#d2b07a 70%,#8b6a48)}
.welcome{left:374px;top:527px;width:646px}
.welcome h2{font-family:"Ubuntu",sans-serif;font-weight:500;font-size:21px;color:#222}
.welcome p{font-size:12.7px;line-height:19.2px;color:#444;margin-top:10px;text-align:justify}
.more{left:946px;top:660px;font-family:"Ubuntu",sans-serif;font-style:italic;font-size:12px;color:var(--teal-dark)}
.rule{left:378px;top:687px;width:642px;border-top:1px dotted #bbb}
.scroll-title{left:381px;top:699px;font-family:"Ubuntu",sans-serif;font-weight:500;font-size:20px;color:var(--maroon)}
.listing-bar{left:380px;top:737px;width:648px;height:34px;background:var(--teal-dark);border-radius:4px;color:#fff;font-family:"Ubuntu",sans-serif;font-weight:500;font-size:16px;line-height:34px;padding-left:8px}
.thumb{left:384px;top:793px;width:143px;height:96px;background:linear-gradient(#6c8aa8,#c9ccd0 55%,#6d7a55);border:3px solid #444}
.details{left:383px;top:902px;width:144px;height:30px;background:linear-gradient(#555,#111);border-radius:6px;color:#fff;font-family:"Ubuntu",sans-serif;font-weight:700;font-size:16px;display:flex;align-items:center;gap:10px;padding-left:18px}
.lot{left:545px;top:792px;width:490px}
.lot h3{font-family:"Ubuntu",sans-serif;font-weight:500;font-size:16.5px;color:var(--maroon);white-space:nowrap}
.lot .meta{font-size:13px;line-height:17.5px;color:#333;margin-top:8px;letter-spacing:.3px}
.lot h4{font-family:"Ubuntu",sans-serif;font-weight:500;font-size:16px;color:var(--teal);margin-top:10px}
.bid-btn{left:546px;top:983px;width:347px;height:40px;background:linear-gradient(#555,#0d0d0d);border-radius:6px;color:#fff;font-weight:700;font-size:16.5px;display:flex;align-items:center;gap:14px;padding-left:12px}
.bid-btn i{width:26px;height:22px;background:#2e7d6e;border:2px solid #ddd;display:block}
.footer{left:0;top:1120px;width:1133px;height:80px;background:var(--dark);border-top:4px solid #fff}
.footer nav{position:absolute;left:100px;top:26px;font-size:12px;color:#fff}
.footer nav a{color:#fff;text-decoration:none}
.footer nav em{font-style:normal;margin:0 8px}
.footer p{position:absolute;left:101px;top:52px;font-size:12px;color:#fff}
.footer-brand{position:absolute;left:938px;top:28px;display:flex;align-items:center;gap:6px;font-family:"Ubuntu",sans-serif;font-weight:700;font-size:14px;color:var(--teal-light)}
.footer-brand i{width:14px;height:14px;background:var(--teal-light);display:block}
</style>
</head>
<body>
<div class="abs topbar"></div>

<header>
  <div class="abs brand"><span class="brand-mark"></span><span class="brand-name">Millbrook<br>Auctions</span></div>
  <div class="abs tagline"><h1>Auction &amp; Real Estate Company</h1><p>Based in California</p></div>
  <div class="abs phone">
    <svg width="38" height="38" viewBox="0 0 38 38"><circle cx="19" cy="19" r="17" fill="none" stroke="#222" stroke-width="2"/><path d="M13 11c2-1 3 0 4 3l-2 2c1 3 3 5 6 6l2-2c3 1 4 2 3 4-1 2-3 3-5 2-6-2-9-6-10-11 0-2 0-3 2-4z" fill="#222"/></svg>
    <span>(123) 456 7890</span>
  </div>
  <div class="abs connect">Get Connected with</div>
  <div class="abs social" aria-label="Social media links"><span aria-label="Social link 1"></span><span aria-label="Social link 2"></span><span aria-label="Social link 3"></span><span aria-label="News feed"></span></div>
</header>

<nav class="abs nav">
  <a href="#">Home</a><a href="#">Auctions</a><a href="#" class="active">Online Auctions</a><a href="#">Past Auctions</a><a href="#">About Us</a><a href="#">FAQ</a><a href="#">Blog</a><a href="#">Contact Us</a>
</nav>

<aside>
  <section class="abs side-box" style="top:215px;height:156px">
    <div class="side-title">SMS Sign Up</div>
    <div class="field abs" style="left:10px;top:47px;width:158px">Your Name</div>
    <div class="field abs" style="left:10px;top:83px;width:158px">Your Name</div>
    <span class="btn-dark abs" style="left:14px;top:123px">Signup Now</span>
    <div class="abs phone-art" role="img" aria-label="Smartphone showing SMS message"></div>
  </section>

  <svg class="abs register" viewBox="0 0 268 218" role="img" aria-label="Register here to join now for free, bid online">
    <rect x="20" y="38" width="236" height="172" rx="8" fill="#f4f4f4" stroke="#ccc" stroke-width="3"/>
    <rect x="26" y="190" width="224" height="14" fill="#0f8a3c"/>
    <circle cx="215" cy="43" r="40" fill="#1faa3c"/>
    <text x="215" y="53" text-anchor="middle" font-family="Ubuntu,sans-serif" font-weight="700" font-size="28" fill="#fff">Free</text>
    <text x="40" y="94" font-family="Ubuntu,sans-serif" font-weight="500" font-size="15" fill="#333">Register here to</text>
    <rect x="4" y="108" width="262" height="40" rx="20" fill="#2ed18a"/>
    <circle cx="26" cy="128" r="16" fill="#222"/>
    <text x="26" y="135" text-anchor="middle" font-family="Ubuntu,sans-serif" font-weight="700" font-size="18" fill="#fff">$</text>
    <text x="48" y="137" font-family="Ubuntu,sans-serif" font-weight="700" font-size="25" fill="#1a1a1a">join now for free</text>
    <text x="136" y="182" text-anchor="middle" font-family="Ubuntu,sans-serif" font-weight="700" font-size="32" fill="var(--teal)">BID ONLINE</text>
  </svg>

  <section class="abs side-box" style="top:626px;height:183px">
    <div class="side-title">Subscribe Newsletter</div>
    <p style="font-size:11.5px;line-height:17.5px;color:#444;padding:8px 6px 0">Subscribe your Email address to get latest newsletters and updates...</p>
    <div class="field abs" style="left:10px;top:94px;width:219px;color:var(--teal)">Enter Your Email Address</div>
    <span class="btn-dark abs" style="left:65px;top:141px">Subscribe Now</span>
  </section>

  <section class="abs side-box" style="top:828px;height:266px">
    <div class="side-title">News &amp; Events</div>
    <div style="padding:3px 10px 0 6px">
      <div class="news-item">Lorem ipsum dolor sit amet, consectetuer adipiscing elit. Nam cursus...</div>
      <div class="news-item">Lorem ipsum dolor sit amet, consectetuer adipiscing elit. Nam cursus...</div>
      <div class="news-item" style="border:0">Lorem ipsum dolor sit amet, consectetuer adipiscing elit. Nam cursus...</div>
    </div>
    <svg class="abs" style="left:194px;top:242px" width="30" height="16" viewBox="0 0 30 16"><path d="M9 2L3 8l6 6" fill="none" stroke="#999" stroke-width="3"/><path d="M20 2l6 6-6 6" fill="none" stroke="#111" stroke-width="3"/></svg>
  </section>
</aside>

<main>
  <div class="abs slide"><div class="slide-img" role="img" aria-label="Antique shop interior with furniture, glassware and flowers"></div></div>
  <div class="abs drop">
    <a href="#" class="on">Auction Area 1</a><a href="#">Auction Area 2</a><a href="#">Auction Area 3</a><a href="#">Auction Area 4</a>
  </div>

  <section class="abs welcome">
    <h2>WELCOME TO MILLBROOK AUCTIONS</h2>
    <p>simply dummy text of the printing and typesetting industry. Lorem Ipsum has been the industry's standard dummy text ever since the 1500s, when an unknown printer took a galley of type and scrambled it to make a type speci men book. It has survived not only five centuries, but also a galley of type and scrambled the leap into electronic typesetting, remaining essen tially unchanged. It was popularised in the 1960s with the release of Letraset sheets containing Lorem Ipsum passages.</p>
  </section>
  <div class="abs more">More Details &#187;</div>
  <div class="abs rule"></div>

  <h2 class="abs scroll-title">Live &amp; Online Auctions Scroll Down</h2>
  <div class="abs listing-bar">HOLLIS PHYSICAL THERAPY IN ASHGROVE, GA</div>

  <div class="abs thumb" role="img" aria-label="Silver minivan parked outdoors"></div>
  <div class="abs details">
    <svg width="20" height="20" viewBox="0 0 20 20"><circle cx="12" cy="8" r="6" fill="none" stroke="#fff" stroke-width="2"/><path d="M8 12l-6 6" stroke="#fff" stroke-width="3"/><path d="M12 5v6M9 8h6" stroke="#fff" stroke-width="1.6"/></svg>DETAILS
  </div>

  <div class="abs lot">
    <h3>Dale Harmon Auctions, LLC GAL 4812 - Everything high bidder.</h3>
    <div class="meta"><b>Location:</b><br>Location 1 - 412 Larkspur Hwy<br>Location 2 - 58 Creek Mdws # 2<br>Ashgrove, GA 30618</div>
    <h4>Online Bidding Only</h4>
    <div class="meta" style="margin-top:6px"><b>Began:</b>&nbsp; Friday, May 24, 2013 at 10:06 AM EDT<br><b>Ends:</b>&nbsp; Wednesday, June 05, 2013 at 10:00 AM EDT</div>
  </div>
  <div class="abs bid-btn"><i></i>Click here for Online Bidding</div>
</main>

<footer class="abs footer">
  <nav><a href="#">Home</a><em>|</em><a href="#">Auctions</a><em>|</em><a href="#">Online Auctions</a><em>|</em><a href="#">Past Auctions</a><em>|</em><a href="#">About Us</a><em>|</em><a href="#">FAQ</a><em>|</em><a href="#">Blog</a><em>|</em><a href="#">Contact Us</a></nav>
  <p>Copyright (C) Millbrook Auctions. 2013.&nbsp; All Rights Reserved</p>
  <div class="footer-brand"><i></i>Millbrook Auctions</div>
</footer>
</body>
</html>
```